Business Card Design

Business sales of reconditioned / used batteries with mobile delivery and install services. Customers base majority are auto car sales lots and individuals.

Card need to convey quality product reliability and quick prompt professional service.

Card must reflect excellence in customer care and product being offered

Target Market(s)

Auto car lots new and used. Auto repair shops. Individuals.

Industry/Entity Type

Business

Contact Information for Business Card

Batteries Q-Volt
Cars, Trucks, Boats, Motorcycles, lawn mowers, power tools
Delivery & install available most vehicles
Mon-Sat 9-6pm
Dale Morrick 501-738-2056
*product warranty 6 month shelf life battery/1 year blems battery

```html
<!DOCTYPE html>
<html lang="en">
<head>
<meta charset="utf-8">
<title>Batteries Q-Volt – Business Card</title>
<link href="https://fonts.googleapis.com/css2?family=Questrial&display=swap" rel="stylesheet">
<style>
  :root {
    --card-black: #050505;
    --band-red: #e8141b;
    --text-white: #f2f2f2;
    --text-grey: #b9b9b9;
    --rule-grey: #5a5a5a;
    --backdrop: #d6d6d6;
  }
  * { margin: 0; padding: 0; box-sizing: border-box; }
  html, body {
    width: 1200px; height: 1000px; overflow: hidden;
    background: var(--backdrop);
    font-family: "Questrial", "Century Gothic", sans-serif;
  }
  .canvas { position: relative; width: 1200px; height: 1000px; }
  .business-card {
    position: absolute; left: 120px; top: 226px;
    width: 960px; height: 548px;
    background: var(--card-black);
    color: var(--text-white);
    box-shadow: 0 12px 40px rgba(0,0,0,.25);
    overflow: hidden;
  }
  .brand {
    position: absolute; left: 48px; top: 48px;
    display: flex; align-items: center; gap: 18px;
  }
  .brand-mark { width: 34px; height: 34px; background: var(--band-red); }
  .brand-name { font-size: 42px; letter-spacing: .5px; color: var(--text-white); }
  .brand-rule {
    position: absolute; left: 48px; top: 108px; width: 400px;
    height: 1px; background: var(--rule-grey);
  }
  .hours {
    position: absolute; left: 60px; top: 300px;
    font-size: 21px; color: var(--text-grey); letter-spacing: .3px;
  }
  .warranty-band {
    position: absolute; left: 0; right: 0; top: 338px; height: 46px;
    background: var(--band-red);
    display: flex; align-items: center; padding-left: 60px;
    font-size: 22px; color: var(--text-white); letter-spacing: .3px;
  }
  .warranty-band::before {
    content: ""; position: absolute; left: 110px; top: -10px;
    border-left: 10px solid transparent; border-right: 10px solid transparent;
    border-bottom: 10px solid var(--band-red);
  }
  .contact {
    position: absolute; right: 56px; top: 150px; width: 400px;
    text-align: right; font-size: 19px; color: var(--text-grey);
  }
  .contact-name { display: flex; justify-content: flex-end; align-items: center; gap: 8px; color: var(--text-white); margin-bottom: 14px; }
  .pin { width: 14px; height: 18px; }
  .service-list { list-style: none; }
  .service {
    display: flex; align-items: center; gap: 10px; margin-bottom: 6px;
  }
  .service::before {
    content: ""; width: 6px; height: 6px; border-radius: 50%;
    background: var(--text-grey); flex: none;
  }
  .service .leader { flex: 1; height: 1px; background: var(--rule-grey); }
  .bottom-rule {
    position: absolute; left: 48px; right: 56px; bottom: 70px;
    height: 1px; background: var(--rule-grey);
  }
</style>
</head>
<body>
<main class="canvas">
  <section class="business-card">
    <div class="brand">
      <span class="brand-mark"></span>
      <span class="brand-name">Batteries Q-Volt</span>
    </div>
    <div class="brand-rule"></div>

    <div class="contact">
      <p class="contact-name">
        <svg class="pin" viewBox="0 0 14 18"><path d="M7 0a7 7 0 0 0-7 7c0 5 7 11 7 11s7-6 7-11a7 7 0 0 0-7-7zm0 10a3 3 0 1 1 0-6 3 3 0 0 1 0 6z" fill="#f2f2f2"/></svg>
        Dale Morrick 501-738-2056
      </p>
      <ul class="service-list">
        <li class="service"><span class="leader"></span>Cars</li>
        <li class="service"><span class="leader"></span>Trucks Boats</li>
        <li class="service"><span class="leader"></span>Motorcycles Lawn</li>
        <li class="service"><span class="leader"></span>Mowers</li>
        <li class="service"><span class="leader"></span>Power Tools</li>
      </ul>
    </div>

    <p class="hours">Delivery &amp; Install&nbsp; Mon-Sat 9-6pm</p>
    <div class="warranty-band">*Product Warranty 6 month shelf life battery/1 year blems battery</div>
    <div class="bottom-rule"></div>
  </section>
</main>
</body>
</html>
```